Grindstones- Tattoos/Piercings/Motorcycle/Biker Appearl Shop

Grindstones' buisness cards can be creative, playful and eye catching. Incorporate leather or diamond plate. We are an all female business. Biker theme, Tattoo Photos, Piercing Photos, Diamond plate, Leather and Girls!

This project needs to be an appointment card as well for the tattoo artists and piercers. We need a section that says APPT With: _______ , DATE, TIME, and then a QUOTE and DEPOSIT section for the artists. I attached the logo so you could incorportate that and have complete creative freedom. It's a biker store, we sell biker appearl and accessories, with a tattoo and piercing shop connected. Girls, Leather, Tattoos and Piercings. Have fun with it!
Updates

I've Updated project details for better description of what im looking for. Thanks!

Target Market(s)

Male and Female Ages 15-90. Interests in custom tattoos and quality piercings, bikers, motorcycle accessories like helmets, gloves, masks, leather, boots. Jewlery and clothes.

Industry/Entity Type

Business

Contact Information for Business Card

The business is called Grindstones, address, phone number and website. (2847 Larkmoor Rd. Muskegon, MI. 49517 (231)870-4152 www.inkvalleyshop.example)

Font styles to use
Serif
Sans Serif
Decorative
Script

Requirements
Must have
• Appointment with______
• Date_____ or MON TUES WED THUR etc... check mark boxes
• Time_____
• Quote______
• Deposit_______
• (231) 870-4152
• 2847 Larkmoor Rd
• Muskegon, MI 49517
• a facebook logo
Nice to have
• Owner Roy Pemberly
Should not have
• Tribal dragons or anything Tribal.That's cheesy! No Butterflies, No stars. No boys,

```html
<!DOCTYPE html>
<html lang="en">
<head>
<meta charset="utf-8">
<title>Grindstones – Appointment Card</title>
<link href="https://fonts.googleapis.com/css2?family=Pirata+One&family=Quicksand:wght@400;500&display=swap" rel="stylesheet">
<style>
  :root{
    --backdrop:#d9d9d9;
    --card-white:#ffffff;
    --card-black:#050505;
    --teal:#6fc3c2;
    --teal-light:#b5e2e1;
    --teal-deep:#4a9c9c;
    --ink:#1c1c1c;
    --rule:#bdbdbd;
  }
  *{box-sizing:border-box;margin:0;padding:0}
  html,body{width:1200px;height:1000px;overflow:hidden}
  body{background:var(--backdrop);position:relative;font-family:"Quicksand",sans-serif}

  .card{position:absolute;left:250px;width:700px;height:400px;
        box-shadow:0 6px 18px rgba(0,0,0,.25)}
  .card--front{top:70px;background:var(--card-white);color:var(--ink)}
  .card--back{top:530px;background:var(--card-black);
              display:flex;align-items:center;justify-content:center}

  .ornament{position:absolute;width:150px;height:100px;border-radius:8px;
            background:linear-gradient(135deg,var(--teal-light) 0%,var(--teal) 55%,var(--teal-deep) 100%)}
  .ornament--top{left:40px;top:40px}
  .ornament--bottom{right:40px;bottom:40px}

  .website{position:absolute;top:26px;left:0;right:0;text-align:center;font-size:15px;letter-spacing:.5px}
  .owner{position:absolute;top:56px;left:0;right:0;text-align:center;
         font-family:"Pirata One",serif;font-size:34px;font-weight:400}
  .address{position:absolute;top:104px;left:0;right:0;text-align:center;
           color:var(--teal);font-size:22px;line-height:27px}
  .appt{position:absolute;top:166px;left:210px;width:300px;display:flex;align-items:flex-end;font-size:19px}
  .appt i{flex:1;border-bottom:2px solid var(--rule);margin:0 0 6px 10px}

  .fields{position:absolute;top:204px;left:210px;width:300px;list-style:none}
  .fields li{display:flex;align-items:flex-end;height:36px;color:var(--teal);font-size:18px}
  .fields li span{width:78px}
  .fields li i{flex:1;border-bottom:2px solid var(--rule);margin-bottom:6px}
  .fields li:nth-child(1){padding-left:66px}
  .fields li:nth-child(2){padding-left:44px}
  .fields li:nth-child(3){padding-left:22px}

  .phone{position:absolute;right:40px;top:168px;font-size:19px;letter-spacing:1px}

  .brand-name{font-family:"Pirata One",serif;font-size:120px;color:var(--teal);letter-spacing:4px}
</style>
</head>
<body>

<section class="card card--front">
  <div class="ornament ornament--top" role="img" aria-label="Teal ornamental illustration with dark swirl pattern"></div>
  <div class="ornament ornament--bottom" role="img" aria-label="Teal ornamental illustration with dark swirl pattern"></div>

  <p class="website">www.inkvalleyshop.example</p>
  <h1 class="owner">Owner Roy Pemberly</h1>
  <p class="address">2847 Larkmoor Rd<br>Muskegon, MI 49517</p>
  <p class="appt"><span>Appointment with</span><i></i></p>

  <ul class="fields">
    <li><span>Date</span><i></i></li>
    <li><span>Time</span><i></i></li>
    <li><span>Quote</span><i></i></li>
    <li><span>Deposit</span><i></i></li>
  </ul>

  <p class="phone">(231) 870-4152</p>
</section>

<section class="card card--back">
  <span class="brand-name">Grindstones</span>
</section>

</body>
</html>
```